依頼詳細
会社の宣伝 周りの住民が見やすいもの(工事現場に掲げる工事用防災シート)

楽しく明るい自然のイメージ(緑、木々、空、地球)

イメージカラーはロゴのグリーン

イメージは、ホームページを参考にする
http://hinoda-kensetsu.jp/
記載項目
デザイン指示書に記載しております。
希望イメージ
シンプル 複雑
単色 カラフル
暗い 明るい
日常 高級
遊び心 厳粛
未来的 伝統的
女性的 男性的
希望する色
緑系
納品ファイル
• 高解像度JPG (.jpg)
• イラストレーター形式 (.ai)
補足説明
大変申し訳ありません。
依頼詳細間違えてしまいました。

読みやすく、持っててうれしくなるもの

楽しく明るい自然のイメージ(緑、木々、空、地球)

イメージカラーはロゴのグリーン

イメージは、ホームページを参考にする
■ 選んだ理由

お客様も大変多くのデザインに悩まれておりました。
その中でもイメージしていたものにとても近いデザインをしていただき、選ばせていただきました。素晴らしいデザインありがとうございました。

■ 提案者全員のお礼・コメント

多くのデザインをご提出頂き感謝申し上げます。今後もデザインコンペを行ってまいりますのでよろしくお願い申し上げます。

```html
<!DOCTYPE html>
<html lang="ja">
<head>
<meta charset="utf-8">
<title>日野田建設株式会社 名刺</title>
<link href="https://fonts.googleapis.com/css2?family=Noto+Sans+JP:wght@400;500;700&display=swap" rel="stylesheet">
<style>
  :root {
    --brand-green: #1f9a3e;
    --text-dark: #333333;
    --sky-top: #9fc7ea;
    --sky-mid: #e6f1fa;
    --grass-light: #9fd36a;
    --grass-deep: #4b9a2a;
    --page-bg: #ffffff;
  }
  * { margin: 0; padding: 0; box-sizing: border-box; }
  html, body { width: 875px; height: 1200px; overflow: hidden; background: var(--page-bg); }
  body { font-family: "Noto Sans JP", sans-serif; color: var(--text-dark); position: relative; }

  .card { position: absolute; left: 0; width: 875px; overflow: hidden; }

  /* front side */
  .card-front { top: 0; height: 570px; }
  .nature-scene {
    position: absolute; inset: 0;
    background: linear-gradient(180deg, var(--sky-top) 0%, var(--sky-mid) 30%, #ffffff 55%, #f3f9ee 72%, var(--grass-light) 84%, var(--grass-deep) 100%);
  }
  .philosophy-title {
    position: absolute; top: 118px; left: 0; width: 100%;
    text-align: center; font-size: 31px; font-weight: 500; letter-spacing: 2px;
  }
  .philosophy-list { position: absolute; top: 198px; left: 30px; list-style: none; }
  .philosophy-list li { font-size: 17.5px; line-height: 51px; white-space: nowrap; }
  .philosophy-list b { font-weight: 700; }

  /* back side */
  .card-back { top: 598px; height: 602px; background: var(--page-bg); }
  .brand { position: absolute; top: 25px; left: 30px; display: flex; align-items: center; gap: 10px; }
  .brand-mark { width: 24px; height: 24px; background: var(--brand-green); }
  .brand-name { font-size: 24px; font-weight: 700; color: var(--brand-green); letter-spacing: 1px; }
  .brand-rule { position: absolute; top: 64px; left: 30px; right: 25px; height: 3px; background: var(--brand-green); }

  .label-box {
    position: absolute; left: 30px; width: 130px;
    background: var(--brand-green); color: #fff;
    display: flex; align-items: center; justify-content: center; text-align: center;
    font-size: 22px; line-height: 1.35; font-weight: 500;
  }
  .label-contact { top: 145px; height: 160px; }
  .label-accident { top: 345px; height: 90px; }

  .info { position: absolute; left: 190px; font-size: 22px; line-height: 43px; white-space: nowrap; }
  .info-contact { top: 70px; }
  .info-accident { top: 354px; }
  .info-emergency { top: 455px; }
  .row { display: flex; }
  .row .key { width: 110px; }
  .info-accident .name { width: 395px; }
  .info-emergency .name { width: 200px; }
  .info-emergency .name.wide { width: 200px; }
</style>
</head>
<body>

<section class="card card-front">
  <div class="nature-scene" role="img" aria-label="明るい青空と緑の草原の風景"></div>
  <h1 class="philosophy-title">企業理念</h1>
  <ol class="philosophy-list">
    <li>1. <b>幸福の追求</b>（会社員が物心両面で豊かな会社にします）</li>
    <li>2. <b>貢献</b>（地域開発の担い手として確かな技術を持って社会の繁栄に貢献します）</li>
    <li>3. <b>挑戦</b>（どんな困難な仕事にもみんなで力を合わせ挑戦します）</li>
    <li>4. <b>感謝</b>（お客様・家族・社会・社員　すべてに感謝します）</li>
  </ol>
</section>

<section class="card card-back">
  <div class="brand">
    <span class="brand-mark"></span>
    <span class="brand-name">日野田建設株式会社</span>
  </div>
  <div class="brand-rule"></div>

  <div class="label-box label-contact">会社<br>連絡先</div>
  <div class="info info-contact">
    <div>〒321-0456 栃木県緑ヶ丘市大字若葉台 512-8</div>
    <div class="row"><span class="key">TEL</span><span>0281-40-1357</span></div>
    <div class="row"><span class="key">FAX</span><span>0281-40-2468</span></div>
    <div class="row"><span class="key"></span><span>090-1234-5678（常務）</span></div>
    <div class="row"><span class="key">URL</span><span>http://hinoda-kensetsu.jp/</span></div>
    <div class="row"><span class="key">Email</span><span>info@hinoda-kensetsu.jp</span></div>
  </div>

  <div class="label-box label-accident">交通<br>事故</div>
  <div class="info info-accident">
    <div class="row"><span class="name">1. みどり損害保険</span><span>0120-000-111</span></div>
    <div class="row"><span class="name">2. 若葉ビジネスセンター</span><span>0281-41-7788</span></div>
  </div>

  <div class="info info-emergency">
    <div class="row"><span class="name">緑ヶ丘警察署</span><span>0281-30-0110</span></div>
    <div class="row"><span class="name">緑ヶ丘消防署</span><span>0281-39-1190</span></div>
    <div class="row"><span class="name wide">緑ヶ丘市防災対策課</span><span>0281-39-1191</span></div>
  </div>
</section>

</body>
</html>
```